Logo & Visitenkarte für Gesundheit
Zielgruppe
Gesundheitsprodukte
Ernährungsberatung
Aufgabenstellung
nicht spezifisch Logo mit Essen und Trinken. Eher ein allgemeines Logo für Gesundheit

```html
<!DOCTYPE html>
<html lang="de">
<head>
<meta charset="utf-8">
<title>Visitenkarten – Vital</title>
<link href="https://fonts.googleapis.com/css2?family=Roboto:wght@400;700&family=Open+Sans:wght@400&display=swap" rel="stylesheet">
<style>
  :root {
    --backdrop: #e7e8ea;
    --teal: #003335;
    --teal-muted: #4d6a68;
    --lime: #b5c21b;
    --white: #ffffff;
  }
  * { margin: 0; padding: 0; box-sizing: border-box; }
  html, body { width: 1200px; height: 754px; overflow: hidden; }
  body {
    background: var(--backdrop);
    position: relative;
    font-family: "Roboto", Arial, sans-serif;
  }
  .card {
    position: absolute;
    width: 414px;
    height: 268px;
  }
  .card--back { background: var(--teal); top: 61px; }
  .card--front { background: var(--white); top: 415px; }
  .pos-left { left: 104px; }
  .pos-right-back { left: 684px; }
  .pos-right-front { left: 683px; }

  /* back side */
  .back-mark {
    position: absolute;
    display: flex;
    align-items: center;
    gap: 10px;
  }
  .back-mark--centered { left: 0; right: 0; top: 100px; justify-content: center; }
  .back-mark--corner { left: 26px; top: 90px; }
  .back-mark__dot {
    width: 22px; height: 22px; border-radius: 50%;
    background: var(--lime);
    flex: none;
  }
  .back-mark__name {
    color: var(--teal-muted);
    font-weight: 700;
    font-size: 24px;
    line-height: 1.05;
    letter-spacing: 0.5px;
  }
  .back-url {
    position: absolute;
    left: 0; right: 0; top: 241px;
    text-align: center;
    color: var(--white);
    font-family: "Open Sans", Arial, sans-serif;
    font-size: 10.5px;
  }

  /* front side */
  .brand {
    position: absolute;
    left: 21px; top: 26px;
    display: flex; align-items: center; gap: 10px;
  }
  .brand__dot {
    width: 30px; height: 30px; border-radius: 50%;
    background: var(--lime);
    flex: none;
  }
  .brand__name {
    color: var(--teal);
    font-weight: 700;
    font-size: 21px;
    line-height: 1.05;
    letter-spacing: 0.5px;
  }
  .person { position: absolute; left: 21px; top: 127px; color: var(--teal); }
  .person__name { font-weight: 700; font-size: 17.5px; line-height: 1.1; }
  .person__role { font-size: 13.5px; line-height: 1.15; }

  .contact-band {
    position: absolute;
    left: 0; right: 0; top: 171px; height: 74px;
    background: var(--teal);
    color: var(--white);
    font-size: 12.5px;
  }
  .address { position: absolute; left: 21px; top: 15px; line-height: 18px; }
  .reach { position: absolute; left: 204px; top: 8px; list-style: none; }
  .reach li { display: flex; align-items: center; height: 20px; }
  .reach svg { width: 18px; height: 16px; margin-right: 10px; flex: none; }
</style>
</head>
<body>

  <section class="card card--back pos-left">
    <div class="back-mark back-mark--centered">
      <span class="back-mark__dot"></span>
      <span class="back-mark__name">VITAL FOR<br>EVERY DAY</span>
    </div>
    <p class="back-url">www.vitalforeveryday.de</p>
  </section>

  <section class="card card--back pos-right-back">
    <div class="back-mark back-mark--corner">
      <span class="back-mark__dot"></span>
      <span class="back-mark__name">VITAL IS<br>EVERY DAY</span>
    </div>
    <p class="back-url">www.vitalforeveryday.de</p>
  </section>

  <section class="card card--front pos-left">
    <div class="brand">
      <span class="brand__dot"></span>
      <span class="brand__name">VITAL FOR<br>EVERY DAY</span>
    </div>
    <div class="person">
      <p class="person__name">MAX MUSTERMAN</p>
      <p class="person__role">Function</p>
    </div>
    <div class="contact-band">
      <p class="address">Streetnumber 00<br>City name</p>
      <ul class="reach">
        <li><svg viewBox="0 0 18 16"><path d="M7 1c2 0 3 1 2 3l-1 2c1 2 2 3 3 4l2-1c2-1 3 0 3 2-2 3-6 3-9-1S4 3 7 1z" fill="var(--white)"/></svg>000000000000</li>
        <li><svg viewBox="0 0 18 16"><rect x="1" y="3" width="16" height="11" fill="none" stroke="var(--white)" stroke-width="1.6"/><path d="M1 3l8 6 8-6M1 14l6-5M17 14l-6-5" fill="none" stroke="var(--white)" stroke-width="1.4"/></svg>info@vitalisbetter.de</li>
        <li><svg viewBox="0 0 18 16"><g fill="none" stroke="var(--white)" stroke-width="1.2"><circle cx="9" cy="8" r="7"/><ellipse cx="9" cy="8" rx="3" ry="7"/><path d="M2 8h14M3 4.5h12M3 11.5h12"/></g></svg>www.vitalisbetter.de</li>
      </ul>
    </div>
  </section>

  <section class="card card--front pos-right-front">
    <div class="brand">
      <span class="brand__dot"></span>
      <span class="brand__name">VITAL IS<br>EVERY DAY</span>
    </div>
    <div class="person">
      <p class="person__name">MAX MUSTERMAN</p>
      <p class="person__role">Function</p>
    </div>
    <div class="contact-band">
      <p class="address">Streetnumber 00<br>City name</p>
      <ul class="reach">
        <li><svg viewBox="0 0 18 16"><path d="M7 1c2 0 3 1 2 3l-1 2c1 2 2 3 3 4l2-1c2-1 3 0 3 2-2 3-6 3-9-1S4 3 7 1z" fill="var(--white)"/></svg>000000000000</li>
        <li><svg viewBox="0 0 18 16"><rect x="1" y="3" width="16" height="11" fill="none" stroke="var(--white)" stroke-width="1.6"/><path d="M1 3l8 6 8-6M1 14l6-5M17 14l-6-5" fill="none" stroke="var(--white)" stroke-width="1.4"/></svg>info@vitalisbetter.de</li>
        <li><svg viewBox="0 0 18 16"><g fill="none" stroke="var(--white)" stroke-width="1.2"><circle cx="9" cy="8" r="7"/><ellipse cx="9" cy="8" rx="3" ry="7"/><path d="M2 8h14M3 4.5h12M3 11.5h12"/></g></svg>www.vitalisbetter.de</li>
      </ul>
    </div>
  </section>

</body>
</html>
```